Discreet simple classy for adult entertainment

I would like a matte black business card with gold writing for my business. Keeping it simple. Having my following:

Lana frost
Events. Entertainment. Promotions
0491726580

or alternatively could have what i had on my previous card below but i think i prefer the above as again - discretion.

Maybe a nice gold line thru the card or some other very simple design . Or not open to ideas/ can be doublesided if any good ideas with that.

included pics of my old bus card. not sure weather i want a photo on it or not. if i do it wont be the same pic. i kinda wanted a card that was discreet so if it was in someones wallet they wouldn't neccessarily realise it was from a stripper.

Target Market(s)

men

Industry/Entity Type

Business

Contact Information for Business Card

Lana frost
0491726580

Requirements
Nice to have
• i don't know i am really open to anything. im giving my cards to guys so something they can have in their wallet that is discreet preferably.

```html
<!DOCTYPE html>
<html lang="en">
<head>
<meta charset="utf-8">
<title>Lana Frost – Business Card</title>
<link href="https://fonts.googleapis.com/css2?family=Poppins:wght@600&family=Questrial&display=swap" rel="stylesheet">
<style>
  :root {
    --card-bg: #272727;
    --gold: #f7ad2f;
    --stage-light: #e9e9e9;
    --stage-mid: #7a7a7a;
    --crowd-dark: #1b1b1b;
  }
  html, body {
    margin: 0;
    padding: 0;
    width: 1200px;
    height: 706px;
    overflow: hidden;
    background: var(--card-bg);
  }
  .card {
    position: relative;
    width: 1200px;
    height: 706px;
    background: var(--card-bg);
    overflow: hidden;
  }
  .concert-photo {
    position: absolute;
    left: 660px;
    top: 150px;
    width: 540px;
    height: 556px;
    background:
      radial-gradient(ellipse 150px 110px at 300px 185px, var(--stage-light) 0%, rgba(200,200,200,0.7) 40%, rgba(120,120,120,0) 100%),
      radial-gradient(ellipse 260px 200px at 300px 200px, rgba(122,122,122,0.55) 0%, rgba(60,60,60,0.25) 60%, rgba(39,39,39,0) 100%),
      linear-gradient(to bottom, rgba(39,39,39,0) 0%, rgba(39,39,39,0) 48%, var(--crowd-dark) 60%, #2a2a2a 100%);
    -webkit-mask-image: linear-gradient(to right, transparent 0%, #000 28%);
    mask-image: linear-gradient(to right, transparent 0%, #000 28%);
  }
  .name {
    position: absolute;
    left: 66px;
    top: 46px;
    margin: 0;
    font-family: "Poppins", sans-serif;
    font-weight: 600;
    font-size: 92px;
    line-height: 1.1;
    letter-spacing: 1px;
    color: var(--gold);
  }
  .phone {
    position: absolute;
    left: 66px;
    top: 168px;
    margin: 0;
    font-family: "Poppins", sans-serif;
    font-weight: 600;
    font-size: 60px;
    line-height: 1.1;
    color: var(--gold);
  }
  .services {
    position: absolute;
    left: 66px;
    top: 436px;
    margin: 0;
    padding: 0;
    list-style: none;
    font-family: "Questrial", sans-serif;
    font-size: 58px;
    line-height: 72px;
    letter-spacing: 2px;
    color: var(--gold);
  }
</style>
</head>
<body>
  <div class="card">
    <div class="concert-photo" role="img" aria-label="Black and white photo of a lit concert stage with a large crowd in front"></div>
    <h1 class="name">LANA FROST</h1>
    <p class="phone">0491 726 580</p>
    <ul class="services">
      <li>Events</li>
      <li>Entertainment</li>
      <li>Promotions</li>
    </ul>
  </div>
</body>
</html>
```